Ridgeline E-Bike Tours

We are an Electric Mountain bike tour company in New Zealand. We will be offering bike rental and guided tours around the Nelson region in New Zealand. I want our website to represent both Mountain biking and New Zealand with the colours layout and features. We want tabs for the following:
-1 about us
-2 what we offer
-3 bookings/contact
Under the about us tab will be who we are as a a company. I want the ability to add videos to each of these tabs as we move foward with videos of the tracks we will be riding. I want the website to be editable so I can add and remove videos/photos myself. Also "our bikes" will be under this tab.
Under the what we offer tab will be
-1 bike rental and pricing
-2 guided tours and pricing
-3 recommended package deals.
I want to able to put the tracks under the guided tours tab and select beginner/ intermediate/advanced and have the tracks in each of the following to match the rider level. Also to be able to have a small video of the track would be great in this section.
Bookings and contact tab
(Further information for this tab to be updated soon)
Coded - Design and coding required
1 page
- Silver ferns, kiwi, mountains

```html
<!DOCTYPE html>
<html lang="en">
<head>
<meta charset="utf-8">
<title>Ridgeline E-Bike Tours</title>
<link href="https://fonts.googleapis.com/css2?family=Open+Sans:wght@400;600;700&family=Roboto:wght@300;400&display=swap" rel="stylesheet">
<style>
:root{
  --orange:#f15a24;
  --coral:#f07057;
  --ink:#2b2f3a;
  --text:#5b5b5b;
  --muted:#8a8a8a;
  --line:#e2e2e2;
  --sand-l:#ece8e5;
  --sand-r:#e3dfdb;
  --soft:#f4f4f4;
  --navy:#1f2734;
  --white:#ffffff;
}
*{box-sizing:border-box;margin:0;padding:0}
html,body{width:1200px;height:3291px;overflow:hidden}
body{font-family:"Open Sans",Arial,sans-serif;color:var(--text);background:var(--white);position:relative}
section,header,footer{position:relative;width:1200px}
.abs{position:absolute}
.btn{position:absolute;display:flex;align-items:center;justify-content:center;border-radius:22px;font-size:13px;font-weight:600;text-transform:uppercase;letter-spacing:.3px}
.btn-orange{background:var(--orange);color:var(--white)}
.heading{font-family:"Roboto",Arial,sans-serif;font-weight:300;color:var(--ink);text-align:center;position:absolute;left:0;width:100%}

/* top bar */
.topbar{height:26px;background:var(--white);font-size:10px;color:#444}
.topbar nav{position:absolute;left:113px;top:7px;display:flex;gap:22px;text-transform:uppercase}
.topbar nav .current{border-bottom:1px solid #444}
.topbar .contact{position:absolute;right:113px;top:7px;display:flex;gap:18px}
.topbar .contact span::before{content:"";display:inline-block;width:7px;height:7px;border-radius:50%;background:var(--orange);margin-right:5px;vertical-align:middle}

/* hero */
.hero{height:546px;overflow:hidden}
.hero-photo{position:absolute;inset:0;background:linear-gradient(180deg,#1c2420 0%,#2c3529 45%,#3b3622 75%,#221f1a 100%)}
.brand-mark{position:absolute;left:0;width:100%;top:110px;display:flex;justify-content:center;align-items:center;gap:14px;color:var(--white);font-size:46px;font-weight:700}
.brand-mark i{width:26px;height:26px;border-radius:50%;background:var(--white);display:block}
.hero h1{position:absolute;top:290px;width:100%;text-align:center;color:var(--white);font-size:50px;font-weight:700}
.hero .lead{position:absolute;top:370px;width:100%;text-align:center;color:var(--white);font-size:16px;font-weight:600}
.hero .btn{left:503px;top:415px;width:193px;height:42px}
.hero .down{position:absolute;left:592px;top:478px}
.dots{position:absolute;left:1174px;top:255px;display:flex;flex-direction:column;gap:8px}
.dots b{width:9px;height:9px;border-radius:50%;background:#888}
.dots b:first-child{background:var(--orange)}

/* who */
.who{height:505px}
.who h2{position:absolute;left:114px;top:95px;font-family:"Roboto",Arial,sans-serif;font-weight:300;font-size:38px;color:var(--ink)}
.who .tag{position:absolute;left:114px;top:160px;font-size:12px;color:var(--orange)}
.who .tag::before{content:"";display:inline-block;width:18px;height:1px;background:var(--orange);margin-right:10px;vertical-align:middle}
.who p{position:absolute;left:114px;top:190px;width:450px;font-size:12.5px;line-height:22px}
.video-frame{position:absolute;left:614px;top:95px;width:448px;height:254px;border:1px solid #ddd;background:var(--white)}
.video{position:absolute;left:638px;top:73px;width:450px;height:254px;background:linear-gradient(135deg,#4e5f3a,#7a6a45 55%,#b38c5a);box-shadow:0 6px 20px rgba(0,0,0,.3)}
.play{position:absolute;left:817px;top:183px;width:94px;height:32px;background:var(--white);border-radius:4px;display:flex;align-items:center;justify-content:center;gap:8px;font-size:12px;font-weight:600;color:#333}
.play i{width:16px;height:16px;border-radius:50%;background:#e62117;display:block}
.who .btn{left:513px;top:396px;width:174px;height:41px;background:var(--coral);font-weight:400;font-size:15px}
.who .down{position:absolute;left:591px;top:455px}

/* bikes */
.bikes{height:474px;display:flex}
.bike{width:600px;height:474px;position:relative;text-align:center}
.bike:first-child{background:var(--sand-l)}
.bike:last-child{background:var(--sand-r)}
.bike h3{position:absolute;top:46px;width:100%;font-family:"Roboto",Arial,sans-serif;font-weight:400;font-size:24px;color:#333}
.bike p{position:absolute;top:98px;left:120px;width:360px;font-size:11.5px;line-height:20px}
.bike-photo{position:absolute;left:66px;top:173px;width:468px;height:264px;border-radius:40% 40% 10% 10%/30% 30% 10% 10%;background:radial-gradient(ellipse at center,#b7b2ad 0%,rgba(0,0,0,0) 70%)}
.bike:first-child .bike-photo{background:radial-gradient(ellipse at center,#3a3a3a 0%,#8d8a86 45%,rgba(0,0,0,0) 72%)}
.bike:last-child .bike-photo{background:radial-gradient(ellipse at center,#4a4a4a 0%,#a9a7a4 45%,rgba(0,0,0,0) 72%)}

/* offer */
.offer{height:790px}
.offer .heading{top:57px;font-size:37px}
.offer .intro{position:absolute;left:200px;top:130px;width:800px;text-align:center;font-size:12.5px;line-height:25px}
.tabs{position:absolute;top:253px;left:298px;display:flex;gap:12px}
.tabs span{height:26px;border-radius:13px;background:#b9b9b9;color:var(--white);font-size:9.5px;display:flex;align-items:center;justify-content:center;text-transform:uppercase}
.tabs span.active{background:var(--orange)}
.plan{position:absolute;top:314px;width:310px;height:408px;background:var(--white);box-shadow:0 1px 6px rgba(0,0,0,.18);text-align:center}
.plan.featured{box-shadow:0 3px 14px rgba(0,0,0,.35)}
.plan h4{margin-top:23px;font-size:14px;font-weight:400;color:#333;text-transform:uppercase}
.plan h4::after{content:"";display:block;width:30px;height:2px;background:var(--orange);margin:12px auto 0}
.plan .price{margin-top:16px;font-size:44px;color:#222;line-height:50px}
.plan .price sup{font-size:22px;vertical-align:-2px}
.plan .deal{margin-top:14px;height:27px;background:var(--coral);color:var(--white);font-size:10.5px;line-height:27px}
.plan.featured .deal,.plan.last .deal{background:var(--orange)}
.plan ul{list-style:none;margin-top:4px}
.plan li{height:33.5px;line-height:33.5px;font-size:11.5px;color:#444}
.plan li:nth-child(odd){background:#e7e7e7}
.plan .cta{position:absolute;left:78px;top:362px;width:154px;height:35px;border-radius:18px;border:1px solid #ccc;font-size:12.5px;font-weight:600;color:#333;display:flex;align-items:center;justify-content:center}
.plan.featured .cta{background:var(--orange);border-color:var(--orange);color:var(--white)}

/* bookings */
.bookings{height:571px;background:var(--soft)}
.bookings .heading{top:50px;font-size:40px}
.info{position:absolute;left:112px;top:148px;width:400px;font-size:12px}
.info h5{font-size:13px;font-weight:600;color:#222}
.info h5::after{content:"";display:block;width:50px;height:2px;background:var(--orange);margin-top:18px}
.info p{margin-top:18px;line-height:22px}
.info dt{margin-top:14px;color:var(--orange);font-weight:600;font-size:13px}
.info dd{margin-top:4px;font-size:11.5px;color:#444;display:flex;align-items:center;gap:8px}
.info dd svg{flex:none}
.form{position:absolute;left:529px;top:138px;width:559px;height:373px;background:var(--white);border:1px solid #ddd}
.field{position:absolute;font-size:10.5px;color:#555;border-bottom:1px solid var(--line);height:32px;padding-top:8px}
.form .btn{left:30px;top:312px;width:132px;height:36px;background:var(--coral);font-weight:400;font-size:12px}

/* subscribe */
.subscribe{height:144px;background:linear-gradient(180deg,#2a3240,var(--navy))}
.subscribe h6{position:absolute;top:35px;width:100%;text-align:center;color:var(--white);font-size:16px;font-weight:700}
.sub-input{position:absolute;top:89px;height:30px;border-radius:15px;background:var(--white);font-size:9.5px;color:#888;padding:8px 16px}
.subscribe .btn{left:759px;top:89px;width:92px;height:30px;font-size:12px;text-transform:none}

/* footer */
.footer{height:235px;background:linear-gradient(90deg,var(--coral),var(--orange))}
.footer .brand{position:absolute;left:112px;top:94px;display:flex;align-items:center;gap:10px;color:var(--white);font-size:34px;font-weight:700}
.footer .brand i{width:18px;height:18px;border-radius:50%;background:var(--white);display:block}
.footer nav{position:absolute;left:362px;top:55px;display:flex;gap:26px;color:var(--white);font-size:12px}
.footer .rule{position:absolute;left:362px;width:726px;height:1px;background:rgba(255,255,255,.35)}
.footer .meta{position:absolute;left:362px;top:109px;color:var(--white);font-size:11.5px}
.footer .social{position:absolute;left:998px;top:108px;display:flex;gap:8px}
.footer .social i{width:12px;height:12px;border-radius:50%;background:var(--white);display:block}
.footer .copy{position:absolute;left:362px;top:164px;color:var(--white);font-size:10.5px}
.footer .up{position:absolute;left:1068px;top:164px}
</style>
</head>
<body>

<header class="topbar">
  <nav><span>Home</span><span class="current">About us</span><span>What we offer</span><span>Bookings/Contact</span></nav>
  <div class="contact"><span>+00 000 000 0000</span><span>info@domainname.com</span></div>
</header>

<section class="hero">
  <div class="hero-photo" role="img" aria-label="Photo of an electric mountain bike on a forest trail at dusk"></div>
  <div class="brand-mark"><i></i>Ridgeline</div>
  <h1>Electric Mountain Bike</h1>
  <p class="lead">Bike rental &amp; guided tours around the Nelson region in New Zealand</p>
  <div class="btn btn-orange">See what we offer</div>
  <svg class="down" width="16" height="36" viewBox="0 0 16 36"><path d="M8 0v34M1 27l7 7 7-7" stroke="#fff" stroke-width="1.5" fill="none"/></svg>
  <div class="dots"><b></b><b></b><b></b></div>
</section>

<section class="who">
  <h2>Who We Are</h2>
  <div class="tag">Ridgeline E-Bike Tours</div>
  <p>Lorem ipsum dolor sit amet, consectetur adipiscing elit. Ut nec dolor aliquam, vehicula velit nec, fermentum metus. In feugiat sapien nec pharetra molestie. Pellentesque in enim purus. Sed eu nulla a felis blandit suscipit. Nam euismod vulputate diam, quis pulvinar erat. Etiam euismod et nunc a facilisis. Donec sollicitudin purus mi, sed vulputate metus consectetur dictum.</p>
  <div class="video-frame"></div>
  <div class="video" role="img" aria-label="Video still of an orange electric mountain bike beside a trail sign in native bush"></div>
  <div class="play"><i></i>PLAY</div>
  <div class="btn">Our Bikes</div>
  <svg class="down" width="16" height="30" viewBox="0 0 16 30"><path d="M8 0v28M2 22l6 6 6-6" stroke="#aaa" stroke-width="1.2" fill="none"/></svg>
</section>

<section class="bikes">
  <div class="bike">
    <h3>Mountain Bike Name</h3>
    <p>Lorem ipsum dolor sit amet, consectetur adipiscing elit. Ut nec dolor aliquam, vehicula velit nec, fermentum metus. In feugiat sapien nec pharetra molestie.</p>
    <div class="bike-photo" role="img" aria-label="Photo of a black full-suspension electric mountain bike"></div>
  </div>
  <div class="bike">
    <h3>Mountain Bike Name</h3>
    <p>Lorem ipsum dolor sit amet, consectetur adipiscing elit. Ut nec dolor aliquam, vehicula velit nec, fermentum metus. In feugiat sapien nec pharetra molestie.</p>
    <div class="bike-photo" role="img" aria-label="Photo of a silver full-suspension electric mountain bike"></div>
  </div>
</section>

<section class="offer">
  <h2 class="heading">What We Offer</h2>
  <p class="intro">Lorem ipsum dolor sit amet, consectetur adipiscing elit. Ut nec dolor aliquam, vehicula velit nec, fermentum metus. In feugiat sapien nec pharetra molestie. Pellentesque in enim purus. Sed eu nulla a felis blandit suscipit. Nam euismod vulputate diam, quis pulvinar erat. Etiam euismod et nunc a facilisis. Donec sollicitudin purus mi, sed vulputate metus consectetur dictum.</p>
  <div class="tabs">
    <span style="width:182px">Bike rental and pricing</span>
    <span style="width:182px">Guided tours and pricing</span>
    <span class="active" style="width:213px">Recommended package deals</span>
  </div>

  <div class="plan" style="left:112px">
    <h4>Standard</h4>
    <div class="price"><sup>$</sup>8.99</div>
    <div class="deal">Choose this plan &amp; save (0%) $00.00</div>
    <ul><li>Lorem ipsum dolor amet</li><li>Consectetur adipiscing</li><li>Elit Ut nec dolor</li><li>Aliquam vehicula velit nec</li><li>Fermentum metus</li></ul>
    <div class="cta">Let's get started</div>
  </div>
  <div class="plan featured" style="left:445px">
    <h4>Extended</h4>
    <div class="price"><sup>$</sup>18.99</div>
    <div class="deal">Choose this plan &amp; save (0%) $00.00</div>
    <ul><li>Lorem ipsum dolor amet</li><li>Consectetur adipiscing</li><li>Elit Ut nec dolor</li><li>Aliquam vehicula velit nec</li><li>Fermentum metus</li></ul>
    <div class="cta">Let's get started</div>
  </div>
  <div class="plan last" style="left:779px">
    <h4>Platinium</h4>
    <div class="price"><sup>$</sup>27.99</div>
    <div class="deal">Choose this plan &amp; save (0%) $00.00</div>
    <ul><li>Lorem ipsum dolor amet</li><li>Consectetur adipiscing</li><li>Elit Ut nec dolor</li><li>Aliquam vehicula velit nec</li><li>Fermentum metus</li></ul>
    <div class="cta">Let's get started</div>
  </div>
</section>

<section class="bookings">
  <h2 class="heading">Bookings &amp; Contact</h2>
  <div class="info">
    <h5>Please use the form for Booking or Contact</h5>
    <p>Lorem ipsum dolor sit amet, consectetur adipiscing elit. Ut nec dolor aliquam, vehicula velit nec, fermentum metus. In feugiat sapien nec pharetra molestie. Pellentesque in enim purus.</p>
    <dl>
      <dt>Address</dt>
      <dd><svg width="9" height="12" viewBox="0 0 9 12"><path d="M4.5 0a4.5 4.5 0 0 0-4.5 4.5C0 8 4.5 12 4.5 12S9 8 9 4.5A4.5 4.5 0 0 0 4.5 0z" fill="#666"/><circle cx="4.5" cy="4.5" r="1.6" fill="#fff"/></svg>Lorem ipsum dolor sit, Nelson, New Zealand</dd>
      <dt>Email</dt>
      <dd><svg width="12" height="9" viewBox="0 0 12 9"><rect x=".5" y=".5" width="11" height="8" fill="none" stroke="#666"/><path d="M.5.5l5.5 4.5L11.5.5" fill="none" stroke="#666"/></svg>info@domainname.com</dd>
      <dt>Phone</dt>
      <dd><svg width="11" height="11" viewBox="0 0 11 11"><path d="M2 0l2 2.5-1 1.5a6 6 0 0 0 3.5 3.5l1.5-1L11 9l-1.5 2C4.5 11 0 6.5 0 1.5z" fill="#666"/></svg>+00 000 000 0000</dd>
      <dt>Fax Line</dt>
      <dd><svg width="12" height="11" viewBox="0 0 12 11"><rect x="0" y="3" width="12" height="8" fill="#666"/><rect x="3" y="0" width="6" height="4" fill="none" stroke="#666"/></svg>+00 000 000 0000</dd>
    </dl>
  </div>
  <div class="form">
    <div class="field" style="left:30px;top:28px;width:240px">Your Name * (required)</div>
    <div class="field" style="left:290px;top:28px;width:240px">Your Email * (required)</div>
    <div class="field" style="left:30px;top:78px;width:500px">Phone Number</div>
    <div class="field" style="left:30px;top:128px;width:500px">Contact Reason:</div>
    <div class="field" style="left:30px;top:232px;width:500px">Your Message</div>
    <div class="btn">Submit</div>
  </div>
</section>

<section class="subscribe">
  <h6>Subscribe to our updates</h6>
  <div class="sub-input" style="left:349px;width:160px">City</div>
  <div class="sub-input" style="left:518px;width:232px">Email Address</div>
  <div class="btn btn-orange">Submit</div>
</section>

<footer class="footer">
  <div class="brand"><i></i>Ridgeline</div>
  <nav><span>Home</span><span>About Us</span><span>What We Offer</span><span>FAQs</span><span>Booking/Contact Us</span></nav>
  <div class="rule" style="top:90px"></div>
  <div class="meta">+00 000 000 0000 &nbsp;/&nbsp; info@domainname.com &nbsp;/&nbsp; Address: Lorem ipsum dolor sit, Nelson, New Zealand</div>
  <div class="social"><i></i><i></i><i></i><i></i><i></i></div>
  <div class="rule" style="top:145px"></div>
  <div class="copy">© Copyright 2018 Ridgeline E-Bike Tours. All Rights Reserved</div>
  <svg class="up" width="12" height="8" viewBox="0 0 12 8"><path d="M1 7l5-5 5 5" stroke="#fff" stroke-width="1.5" fill="none"/></svg>
</footer>

</body>
</html>
```